Attention Getting Doorhanger Postcard Campaign offering HUGE Rebate on New Construction Homes

I am reestablishing my real estate career in the far North Dallas, TX area and want to offer a rebate on new construction homes to help get me started. I am requesting a doorhanger as my first project but would like a theme that I can carry over to other projects including postcards and other marketing items. I want it to look high end, clean, professional and classy. I am attaching a copy of a flier that I created that needs (no graphic designer here) some prettying up. But this is just to give you an idea of the type of style that is of interest to me.

Target Market(s)

Home buyers for new construction in far north dallas suburbs. Usually a move up buyer.

Industry/Entity Type

Real Estate

Colors

Designer to choose colors to be used in the design.

Requirements
Must have
• Catch phrase, draw attention, classy clean lines, current trend colors of blues and grays. My information, Marston Pryce logo, equal housing and realtor logos. Fine Print: Not intended to solicit homes already listed for sale or buyers already in a buyers agency agreement with another brokerage. Please include offer details as listed in my flier. Again I am interested in a door hanger and the next round would be a flier or postcard.
Nice to have
• Picture of new homes that are in line with what is being built in my area. A few home builders sites: Coastal Beacon, Riverbend Homes, Fenwick Homes, Calloway Homes.

```html
<!DOCTYPE html>
<html lang="en">
<head>
<meta charset="utf-8">
<title>Bright and Beyond – Door Hangers</title>
<link rel="stylesheet" href="https://fonts.googleapis.com/css2?family=Open+Sans:wght@400;600;700&family=Arimo:wght@400;700&display=swap">
<style>
  :root {
    --sky: #4fb3d9;
    --sky-light: #6cc3e3;
    --charcoal: #525458;
    --ink: #5b5d61;
    --paper: #ffffff;
    --stage: #ececec;
    --rule: #e3e3e3;
    --agent-red: #b40f2b;
  }
  * { box-sizing: border-box; margin: 0; padding: 0; }
  html, body { width: 1185px; height: 1200px; overflow: hidden; }
  body { background: var(--stage); position: relative; font-family: "Open Sans", sans-serif; color: var(--ink); }

  .hanger {
    position: absolute; top: 88px; width: 428px; height: 1024px;
    background: var(--paper); border-radius: 8px 8px 0 0; overflow: hidden;
    box-shadow: 0 4px 14px rgba(0,0,0,.18);
  }
  .hanger--offer { left: 135px; }
  .hanger--process { left: 651px; }

  .campaign-title {
    position: absolute; top: 22px; left: 0; right: 0; text-align: center;
    font-family: "Open Sans", sans-serif; font-weight: 700; color: var(--sky);
    font-size: 34px; line-height: 1.1; z-index: 3;
  }

  .photo { position: absolute; left: 0; width: 100%; }
  .photo--home { top: 121px; height: 332px; background: linear-gradient(180deg, #d9c8c6 0%, #eae6e4 35%, #cfcfcf 60%, #5c7a3e 82%, #4a6a30 100%); }
  .photo--field { top: 121px; height: 297px; background: linear-gradient(180deg, #dfe9e6 0%, #eef3ef 40%, #8fbf55 62%, #5e9a2b 100%); }

  .hang-hole { position: absolute; top: 0; left: 0; z-index: 2; }

  .savings-badge { position: absolute; left: 280px; top: 316px; width: 132px; height: 132px; z-index: 2; }
  .savings-badge span {
    position: absolute; inset: 0; display: flex; align-items: center; justify-content: center; text-align: center;
    font-family: "Arimo", sans-serif; font-weight: 700; color: #fff; font-size: 17px; line-height: 1.2;
  }

  .offer-band { position: absolute; top: 453px; left: 0; width: 100%; height: 155px; background: var(--charcoal); color: #fff; text-align: center; font-family: "Arimo", sans-serif; }
  .offer-band h2 { font-weight: 400; font-size: 23px; line-height: 1.16; margin-top: 17px; }
  .offer-band h2 b { font-weight: 700; }
  .offer-band .big { font-weight: 700; font-size: 25px; }
  .example-pill {
    position: absolute; left: 37px; right: 37px; top: 116px; height: 30px; border-radius: 5px;
    background: var(--sky); font-family: "Open Sans", sans-serif; font-size: 14px; line-height: 30px; color: #fff;
  }

  .offer-points { position: absolute; top: 630px; left: 10px; right: 22px; list-style: none; }
  .offer-points li {
    position: relative; padding: 8px 0 8px 24px; font-size: 15px; line-height: 1.4;
    border-bottom: 1px dashed var(--rule);
  }
  .offer-points li:last-child { border-bottom: 0; }
  .offer-points svg { position: absolute; left: 2px; top: 13px; }

  .contact-bar {
    position: absolute; left: 0; bottom: 0; width: 100%; height: 95px; background: var(--sky);
    color: #fff; text-align: center; font-size: 17px; line-height: 27px; padding-top: 20px;
  }
  .contact-bar svg { vertical-align: -3px; margin: 0 3px 0 6px; }

  .package-band { position: absolute; top: 418px; left: 0; width: 100%; height: 93px; background: var(--charcoal); color: #fff; text-align: center; font-family: "Arimo", sans-serif; font-size: 16.5px; line-height: 1.3; padding-top: 17px; }
  .how-pill {
    position: absolute; top: 497px; left: 113px; width: 202px; height: 29px; z-index: 2;
    background: #fff; border-radius: 5px; box-shadow: 0 2px 4px rgba(0,0,0,.25);
    text-align: center; font-size: 14px; line-height: 29px; color: var(--ink); font-weight: 600;
  }
  .steps { position: absolute; top: 511px; left: 0; width: 100%; height: 180px; background: var(--sky); display: flex; justify-content: space-around; padding: 38px 6px 0; }
  .step { width: 100px; text-align: center; color: #fff; font-size: 13px; line-height: 1.4; }
  .step-icon {
    width: 78px; height: 78px; margin: 0 auto 9px; border-radius: 50%;
    border: 3px solid #fff; background: var(--sky-light);
    display: flex; align-items: center; justify-content: center;
  }
  .step-icon i { width: 50px; height: 50px; border-radius: 50%; background: #fff; display: flex; align-items: center; justify-content: center; }

  .testimonial { position: absolute; top: 712px; left: 14px; right: 12px; font-size: 13.5px; line-height: 1.32; }
  .testimonial .mark { font-family: Georgia, serif; font-size: 34px; color: var(--sky); line-height: 0; vertical-align: -12px; font-weight: 700; }

  .agent-photo { position: absolute; top: 806px; left: 17px; width: 116px; height: 116px; border-radius: 6px; background: linear-gradient(160deg, #8a6f5c, #2f3442 70%); }
  .agent-card { position: absolute; top: 816px; left: 150px; right: 10px; }
  .brokerage { font-family: "Open Sans", sans-serif; font-weight: 700; color: var(--agent-red); font-size: 17px; display: flex; align-items: center; gap: 8px; }
  .brokerage i { width: 12px; height: 12px; background: var(--agent-red); display: inline-block; }
  .agent-name { margin-top: 14px; font-size: 19px; color: var(--sky); font-weight: 600; }
  .agent-creds { font-size: 13px; color: var(--ink); margin-top: 2px; }
  .member-badges { position: absolute; top: 856px; right: 34px; display: flex; gap: 8px; }
  .member-badges span { width: 26px; height: 26px; background: #55575b; border-radius: 2px; }
</style>
</head>
<body>

<section class="hanger hanger--offer">
  <h1 class="campaign-title">Bright and Beyond</h1>
  <div class="photo photo--home" role="img" aria-label="Photograph of a large white two-storey new construction home with landscaped front lawn at dusk"></div>
  <svg class="hang-hole" width="428" height="200" viewBox="0 0 428 200" aria-hidden="true">
    <path d="M0 121 H120 C150 121 150 186 214 186 C278 186 278 121 308 121 H428 V0 H0Z" fill="var(--paper)"/>
    <circle cx="214" cy="121" r="48" fill="var(--stage)"/>
  </svg>
  <div class="savings-badge">
    <svg width="132" height="132" viewBox="0 0 132 132" aria-hidden="true">
      <polygon fill="var(--sky)" stroke="#fff" stroke-width="2" points="66,2 74,10 84,5 90,14 101,12 104,22 115,24 115,35 124,40 121,50 129,57 124,66 129,75 121,82 124,92 115,97 115,108 104,110 101,120 90,118 84,127 74,122 66,130 58,122 48,127 42,118 31,120 28,110 17,108 17,97 8,92 11,82 3,75 8,66 3,57 11,50 8,40 17,35 17,24 28,22 31,12 42,14 48,5 58,10"/>
    </svg>
    <span>MAXIMIZE<br>YOUR<br>SAVINGS!</span>
  </div>

  <div class="offer-band">
    <h2>Receive a minimum of <b>2.5%</b><br>or more to put towards your<br><span class="big">NEW CONSTRUCTION home!</span></h2>
    <div class="example-pill">For Example: $400,000 equals a $10,000 rebate!</div>
  </div>

  <ul class="offer-points">
    <li><svg width="14" height="12" viewBox="0 0 14 12"><path d="M1 6 L5 10 L13 1" fill="none" stroke="var(--sky)" stroke-width="2"/></svg>We work with 100’s of builders in the local area so you are not limited to a few “select” builders.</li>
    <li><svg width="14" height="12" viewBox="0 0 14 12"><path d="M1 6 L5 10 L13 1" fill="none" stroke="var(--sky)" stroke-width="2"/></svg>Homebuilders have the same bottom line sales price whether you have a REALTOR® representing you or not.</li>
    <li><svg width="14" height="12" viewBox="0 0 14 12"><path d="M1 6 L5 10 L13 1" fill="none" stroke="var(--sky)" stroke-width="2"/></svg>Rebate program will not affect the price you pay for your home.  Brokerage fees are paid through a separate marketing fund, not from the sales price of your home.</li>
    <li><svg width="14" height="12" viewBox="0 0 14 12"><path d="M1 6 L5 10 L13 1" fill="none" stroke="var(--sky)" stroke-width="2"/></svg>Rebate program is in ADDITION to any builder or lender incentives.</li>
  </ul>

  <footer class="contact-bar">
    Saving you!<svg width="16" height="16" viewBox="0 0 16 16"><circle cx="8" cy="8" r="7" fill="none" stroke="#fff" stroke-width="1.4"/><path d="M5.5 4.5 L7 6.5 L6.3 7.4 C6.8 8.5 7.5 9.2 8.6 9.7 L9.5 9 L11.5 10.5 L10.7 11.8 C8 11.6 4.4 8 4.2 5.3Z" fill="#fff"/></svg>469.555.0187<br>danawhitfield@mailbox.com
  </footer>
</section>

<section class="hanger hanger--process">
  <h1 class="campaign-title">Bright and Beyond</h1>
  <div class="photo photo--field" role="img" aria-label="Photograph of a young child jumping joyfully with arms raised in a green grass field"></div>
  <svg class="hang-hole" width="428" height="200" viewBox="0 0 428 200" aria-hidden="true">
    <path d="M0 121 H120 C150 121 150 186 214 186 C278 186 278 121 308 121 H428 V0 H0Z" fill="var(--paper)"/>
    <circle cx="214" cy="121" r="48" fill="var(--stage)"/>
  </svg>

  <div class="package-band">My Buy &amp; List package offers a FLAT FEE<br>on the sale of your current home.</div>
  <div class="how-pill">HOW IT WORKS</div>

  <div class="steps">
    <div class="step">
      <div class="step-icon"><i><svg width="26" height="26" viewBox="0 0 24 24"><path d="M6 3 L9 7 L7.5 9 C8.5 11.5 10.5 13.5 13 14.5 L15 13 L19 16 L17.5 19.5 C11 19 5 13 4.5 6.5Z" fill="var(--sky)"/></svg></i></div>
      Contact Dana<br>to register
    </div>
    <div class="step">
      <div class="step-icon"><i><svg width="28" height="28" viewBox="0 0 24 24"><path d="M3 11 L10 5 L17 11" fill="none" stroke="var(--sky)" stroke-width="2"/><circle cx="11" cy="13" r="4" fill="none" stroke="var(--sky)" stroke-width="2"/><path d="M14 16 L20 22" stroke="var(--sky)" stroke-width="2.5"/></svg></i></div>
      Find your<br>New Home
    </div>
    <div class="step">
      <div class="step-icon"><i><svg width="26" height="26" viewBox="0 0 24 24"><rect x="4" y="4" width="13" height="16" rx="1" fill="none" stroke="var(--sky)" stroke-width="2"/><path d="M9 16 L20 5" stroke="var(--sky)" stroke-width="2.5"/><path d="M7 9 H12 M7 12 H10" stroke="var(--sky)" stroke-width="1.5"/></svg></i></div>
      Sign your<br>Contract
    </div>
    <div class="step">
      <div class="step-icon"><i><svg width="26" height="26" viewBox="0 0 24 24"><path d="M9 3 H15 L13 7 H11Z" fill="var(--sky)"/><path d="M11 7 C5 9 4 14 5 18 C6 21 18 21 19 18 C20 14 19 9 13 7Z" fill="var(--sky)"/><text x="12" y="17.5" text-anchor="middle" font-family="Arimo, sans-serif" font-size="9" font-weight="700" fill="#fff">$</text></svg></i></div>
      Close &amp; Receive<br>your REBATE!
    </div>
  </div>

  <p class="testimonial"><span class="mark">“</span> I’ve sold hundreds of homes in the North Dallas area over the last 13 years, specializing in new construction homes. I would love to help you make your new home dreams a reality.<br>- Dana</p>

  <div class="agent-photo" role="img" aria-label="Portrait photograph of the agent"></div>
  <div class="agent-card">
    <div class="brokerage"><i></i>Marston Pryce</div>
    <div class="agent-name">Dana Whitfield</div>
    <div class="agent-creds">REALTOR®, CRS, ABR, CNHS, CHMS</div>
  </div>
  <div class="member-badges"><span></span><span></span></div>

  <footer class="contact-bar">
    Saving you!<svg width="16" height="16" viewBox="0 0 16 16"><circle cx="8" cy="8" r="7" fill="none" stroke="#fff" stroke-width="1.4"/><path d="M5.5 4.5 L7 6.5 L6.3 7.4 C6.8 8.5 7.5 9.2 8.6 9.7 L9.5 9 L11.5 10.5 L10.7 11.8 C8 11.6 4.4 8 4.2 5.3Z" fill="#fff"/></svg>469.555.0187<br>danawhitfield@mailbox.com
  </footer>
</section>

</body>
</html>
```